lunetra.com redesign

We are a successful web hosting company that has been around since 1999 with 10,000 customers managing 2,000 websites and 12,000 domain names. Our challenge - we are losing ground because our site is getting old, our pricing is not competitive and our feature set needs to change to match the new world of mobile centric everything. We want to reach out to all of the domain names that we don't host websites for. We believe that if we designed a new site that focuses on bringing home all of those externally hosted websites to our own web hosting company that we would have a solid future. We need to compete against mopwizzle.com, vantrimble.com, kerbloom.com, zinqhut.com, nolvark.com, brimfolk.com, quorvane.com, welbix.com and 100,000 others. We need to simplify our message with clean design, focused pages, easy decision making processes for the consumer. We use WHMCS for the background provisioning and billing so we can pretty much manage any kind of pricing model and discounted promotion packages.
I would prefer Twitter bootstrap CSS based responsive design.

Reason: I was away on vacation for 2 weeks - I just got back - I need time to fairly review all submissions - thank you for your patience. Dorian Fenwick Lunetra.com

Thanks to all who submitted sample designs - unfortunately most of them were nothing much more than already available templates with some of my current content and logo added to them. I will try to be more specific to reduce the number of choices. I need the template be fully compatible with WHMCS and Wordpress if you can't make it work with WHMCS directly. Another question I have to ask is -"exactly what am I getting for my $500.00 - is it just a PSD template or actual integration of that theme into WHMCS or Wordpress?"  I don't expect anyone to create new content for the site at that price. What do you charge if  you are able to create content or get directly involved in the site implementation of that template?

```html
<!DOCTYPE html>
<html lang="en">
<head>
<meta charset="utf-8">
<title>Lunetra.com – Discover your own domain</title>
<link href="https://fonts.googleapis.com/css2?family=Open+Sans:wght@400;600;700&display=swap" rel="stylesheet">
<style>
  :root{
    --blue:#00b4f0;
    --blue-text:#1ab0e8;
    --dark:#3b3b3b;
    --dark-band:#444444;
    --orange:#f7a21b;
    --white:#ffffff;
    --text:#333333;
  }
  *{box-sizing:border-box;margin:0;padding:0}
  html,body{width:900px;height:1200px;overflow:hidden;background:var(--white);font-family:"Open Sans",Arial,sans-serif;color:var(--text)}
  .page{position:relative;width:900px;height:1200px;overflow:hidden}

  /* Utility bar */
  .utility-bar{position:absolute;left:0;top:0;width:900px;height:45px;background:var(--dark);color:#cfcfcf;font-size:12px;letter-spacing:.5px}
  .utility-bar span{position:absolute;top:15px;display:flex;align-items:center;gap:7px}
  .utility-bar .divider{position:absolute;left:183px;top:7px;width:1px;height:31px;background:#777}
  .utility-bar svg{fill:#e8e8e8}

  /* Main navigation */
  .main-nav{position:absolute;left:45px;top:45px;width:810px;height:42px;background:var(--blue);display:flex;justify-content:space-around;align-items:center;color:var(--white);font-size:12.5px;font-weight:600;letter-spacing:.4px}

  /* Hero */
  .hero{position:absolute;left:45px;top:87px;width:810px;height:390px;background:linear-gradient(90deg,#f4f4f4 0%,#e6e6e6 55%,#dcdcdc 100%)}
  .brand{position:absolute;left:20px;top:48px;display:flex;align-items:center;gap:12px;font-size:38px;font-weight:700;color:var(--blue);letter-spacing:-.5px}
  .brand i{display:block;width:26px;height:26px;background:var(--blue)}
  .hero h1{position:absolute;left:43px;top:160px;font-size:32px;font-weight:400;color:var(--blue-text);letter-spacing:.8px}
  .domain-search{position:absolute;left:97px;top:227px;width:320px;height:39px;background:var(--blue);padding:5px 18px}
  .domain-search div{width:100%;height:100%;background:var(--white);font-size:12px;color:#9a9a9a;padding:7px 10px}
  .hero-note{position:absolute;left:63px;top:287px;font-size:12px;color:#333}
  .hero-note b{color:var(--blue-text);font-weight:600}
  .hero-photo{position:absolute;right:0;top:0;width:285px;height:390px;background:radial-gradient(ellipse at 55% 45%,#c7a28e 0%,#b9b3ae 35%,#dcdcdc 75%)}

  /* Offer band */
  .offer-band{position:absolute;left:0;top:477px;width:900px;height:281px;background:var(--dark-band)}
  .offer-band .inner{position:absolute;left:45px;top:0;width:810px;height:281px;background:#4a4a4a}
  .slide-arrow{position:absolute;top:132px}
  .guarantee{position:absolute;left:0;width:810px;top:19px;text-align:center;font-size:19px;color:var(--white);letter-spacing:.5px}
  .guarantee b{color:var(--blue-text);font-weight:400;margin-right:14px}
  .promo{position:absolute;left:37px;top:98px;width:250px}
  .promo h2{font-size:18px;color:var(--orange);font-weight:700;white-space:nowrap}
  .promo .price{font-size:19px;color:var(--white);font-weight:600;margin-top:1px}
  .promo h3{font-size:11px;color:var(--orange);font-weight:600;margin-top:14px}
  .plan-list{display:grid;grid-template-columns:88px 130px;gap:3px 0;margin-top:5px;list-style:none;font-size:8px;color:#ddd}
  .plan-list li{display:flex;align-items:center;gap:5px;white-space:nowrap}
  .plan-list li::before{content:"";flex:none;width:7px;height:7px;border-radius:50%;background:#8a6fb5}
  .promo-art{position:absolute;left:300px;top:96px;width:80px;height:118px;background:linear-gradient(180deg,#f6c56a,#f8f1e4 60%,#ffffff)}
  .features{position:absolute;left:442px;top:78px;list-style:none}
  .features li{margin-bottom:17px}
  .features strong{display:block;font-size:16px;font-weight:400;color:var(--white);letter-spacing:.4px}
  .features small{display:block;font-size:8px;color:var(--blue-text)}

  /* Explore strip */
  .explore{position:absolute;left:45px;top:758px;width:810px;height:57px;background:linear-gradient(90deg,#c9c9c9,#f2f2f2 35%,#f2f2f2);text-align:right;padding:15px 38px 0 0;font-size:19px;color:#333;letter-spacing:.4px}
  .explore b{color:var(--blue-text);font-weight:400}

  /* Free services */
  .services-head{position:absolute;left:0;top:815px;width:900px;height:45px;background:var(--blue);color:var(--white);text-align:center;font-size:19px;font-weight:400;padding-top:9px;letter-spacing:.5px}
  .services-icons{position:absolute;left:0;top:860px;width:900px;height:100px;background:linear-gradient(180deg,#dedede,#f4f4f4 50%,#dcdcdc)}
  .services-copy{position:absolute;left:0;top:960px;width:900px;height:132px;background:var(--blue)}
  .service{position:absolute;width:200px;text-align:center}
  .service h4{font-size:13px;font-weight:400;letter-spacing:.6px;color:#333;margin-top:19px}
  .service svg{display:block;margin:10px auto 0}
  .services-icons .rule{position:absolute;top:18px;width:1px;height:62px;background:#888}
  .services-copy p{position:absolute;width:200px;text-align:center;font-size:12px;line-height:18px;color:var(--white);top:24px;white-space:nowrap}

  /* Footer */
  .site-footer{position:absolute;left:45px;top:1092px;width:810px;height:108px;background:var(--dark);text-align:center;color:#ddd}
  .footer-links{margin-top:24px;font-size:8.5px;font-weight:700;color:var(--white);word-spacing:2px}
  .footer-links span{margin:0 3px}
  .copyright{font-size:8.5px;margin-top:1px}
  .legal{font-size:8.5px;margin-top:27px}
  .legal b{color:var(--blue-text);font-weight:400}
</style>
</head>
<body>
<div class="page">

  <header class="utility-bar">
    <span style="left:104px">REGISTER</span>
    <div class="divider"></div>
    <span style="left:204px">SIGN IN
      <svg width="13" height="14" viewBox="0 0 13 14"><circle cx="6.5" cy="4" r="3.2"/><path d="M0 14c0-4 3-6 6.5-6S13 10 13 14z"/></svg></span>
    <span style="left:310px">CART
      <svg width="18" height="14" viewBox="0 0 18 14"><path d="M0 1h3l2.5 8h9L17 3H5" fill="none" stroke="#e8e8e8" stroke-width="1.6"/><circle cx="7" cy="12" r="1.5"/><circle cx="13" cy="12" r="1.5"/></svg></span>
    <span style="left:642px">
      <svg width="15" height="15" viewBox="0 0 15 15"><path d="M3 0l3 3-2 2c1 2 3 4 5 5l2-2 3 3-2 3C6 14 1 9 0 3z"/></svg>
      CUSTOMER SUPPORT</span>
  </header>

  <nav class="main-nav">
    <span>DOMAIN NAME CENTER</span><span>WEB SITE HOSTING CENTER</span><span>SEO TOOL KIT</span><span>SUPPORT</span><span>CLIENT AREA</span>
  </nav>

  <section class="hero">
    <div class="brand"><i></i>lunetra</div>
    <h1>Discover your own domain</h1>
    <div class="domain-search"><div>Your domain name.com</div></div>
    <p class="hero-note">Now <b>get</b> Premium top-level domain names from $15/year.</p>
    <div class="hero-photo" role="img" aria-label="Photo of a smiling woman looking through a magnifying glass"></div>
  </section>

  <section class="offer-band">
    <svg class="slide-arrow" style="left:10px" width="24" height="24" viewBox="0 0 24 24"><path d="M2 12L14 2v6h8v8h-8v6z" fill="#7fc6e6" stroke="#2f6f8f"/></svg>
    <svg class="slide-arrow" style="left:866px" width="24" height="24" viewBox="0 0 24 24"><path d="M22 12L10 2v6H2v8h8v6z" fill="#7fc6e6" stroke="#2f6f8f"/></svg>
    <div class="inner">
      <p class="guarantee"><b>90 day</b>refund guarantee on all purchases</p>
      <div class="promo">
        <h2>Premium Business Hosting</h2>
        <p class="price">From $90/year.</p>
        <h3>Lunetra's e-Lite plan:</h3>
        <ul class="plan-list">
          <li>Domain name</li><li>Unlimited Email Accounts</li>
          <li>100 Mb Space</li><li>Unlimited Aliases</li>
          <li>5 GB Transfer</li><li>Dedicated support</li>
        </ul>
      </div>
      <div class="promo-art" role="img" aria-label="Illustration of stacked server towers"></div>
      <ul class="features">
        <li><strong>Secure your domain</strong><small>Register, renew, transfer or search your domain name</small></li>
        <li><strong>Effective website development</strong><small>Simple site builder, small business bundle and custom design</small></li>
        <li><strong>Web site hosting</strong><small>Realiable, affordable options. Real people – real support</small></li>
        <li><strong>Market your website</strong><small>Professional implementation of Search engine positioning</small></li>
      </ul>
    </div>
  </section>

  <div class="explore"><b>Explore</b> to the world with us</div>

  <h2 class="services-head">GET THESE FREE SERVICES WITH ALL ACCOUNTS</h2>

  <section class="services-icons">
    <div class="service" style="left:57px"><h4>EASY TRANSFER</h4>
      <svg width="36" height="28" viewBox="0 0 36 28"><rect x="1" y="1" width="34" height="26" fill="#e9b65c" stroke="#b98330"/><path d="M12 14h12M20 10l4 4-4 4" stroke="#fff" stroke-width="2" fill="none"/></svg></div>
    <div class="rule" style="left:252px"></div>
    <div class="service" style="left:250px"><h4>SITE BUILDER</h4>
      <svg width="36" height="30" viewBox="0 0 36 30"><rect x="2" y="2" width="30" height="22" fill="#fff" stroke="#666" stroke-width="2"/><path d="M10 22L28 6l3 3-18 16z" fill="#3a8fd0"/></svg></div>
    <div class="rule" style="left:440px"></div>
    <div class="service" style="left:450px"><h4>KITMOUNT</h4>
      <svg width="32" height="34" viewBox="0 0 32 34"><rect x="13" y="0" width="6" height="4" fill="#777"/><circle cx="16" cy="19" r="13" fill="#f3f3f3" stroke="#777" stroke-width="2"/><path d="M16 19V10" stroke="#444" stroke-width="2"/></svg></div>
    <div class="rule" style="left:643px"></div>
    <div class="service" style="left:627px"><h4>SEEKLY</h4>
      <svg width="36" height="30" viewBox="0 0 36 30"><path d="M1 12L35 1 24 29l-7-10z" fill="#8cc63f"/><path d="M17 19L35 1" stroke="#5c8f22" stroke-width="1.5"/></svg></div>
  </section>

  <section class="services-copy">
    <p style="left:57px">Switching to Lunetra<br>from another host<br>is easy: sit back<br>while we take<br>care of everything.</p>
    <p style="left:250px">With SiteBuilder,<br>you can build<br>your website with<br>drag-and-drop<br>simplicity.</p>
    <p style="left:450px">Over 50 essential<br>scripts for building<br>your website installed<br>in minutes with a click</p>
    <p style="left:627px">We include search<br>engine positioning<br>with every plan,<br>so your customers<br>can find your website.</p>
  </section>

  <footer class="site-footer">
    <p class="footer-links"><span>Terms of Use</span><span>Dispute Policy</span><span>Disclaimer</span><span>Privacy Policy</span><span>Refund Policy</span><span>Refund Policy</span><span>Wirenote Newsletter</span></p>
    <p class="copyright">Copyright © 2010 Lunetra.com. All Rights Reserved.</p>
    <p class="legal">All Transactions are based on US or Canadian Dollars. <b>lunetra.com</b> is registered and located in Canada</p>
  </footer>

</div>
</body>
</html>
```